Local Horticulturalist needs Business card design

Meridale Gardening would like to update our existing business card and utilize our new logo (design attached)....we specialize in getting the best out of our customers yard with professional maintenance programs, expert pruning and hedging and garden restorations.
Utilizing colors from attached logo I would like a design that implies professionalism and if possible our businesses love of restoration through plants.
I also sometimes write down for my customers a start date and price on the back of my current card
Target Market(s)
Home owners
Contractors
Industry/Entity Type
Gardener
Contact Information for Business Card
Trevor Kalbrook | Horticulturalist
ph: 0452739186
meridalegard@fernpost.com
www.meridalegardening.com.au
Requirements
Must have
- crucial information easy to read
- incorporate current logo
- Horticulturalist listed preferably near name
Nice to have
- currently I write a job start date and price on the back of my current card so something that integrates this would be beneficial
Should not have
- be pretty or flowerey
- be too white or basic

```html
<!DOCTYPE html>
<html lang="en">
<head>
<meta charset="utf-8">
<title>Meridale Gardening – Business Card</title>
<link href="https://fonts.googleapis.com/css2?family=Lato:wght@400;700&display=swap" rel="stylesheet">
<style>
  :root {
    --stage: #3b322d;
    --card: #161616;
    --card-edge: #222222;
    --leaf-green: #7dc242;
    --bark: #8c7b62;
    --ink-light: #f2f2f2;
    --rule: #2c2c2c;
  }
  * { box-sizing: border-box; margin: 0; padding: 0; }
  html, body {
    width: 1200px; height: 844px; overflow: hidden;
    background: var(--stage);
    font-family: "Lato", sans-serif;
  }
  .canvas {
    position: relative; width: 1200px; height: 844px;
    display: flex; align-items: center; justify-content: center; gap: 44px;
  }
  .card {
    position: relative; width: 525px; height: 300px;
    background: var(--card);
    border: 1px solid var(--card-edge);
    box-shadow: 0 14px 30px rgba(0,0,0,.45);
  }

  /* Front */
  .front-brand {
    position: absolute; left: 0; top: 0; width: 190px; height: 100%;
    display: flex; flex-direction: column; align-items: center; justify-content: center; gap: 14px;
  }
  .brand-dot {
    width: 64px; height: 64px; border-radius: 50%;
    background: var(--leaf-green);
  }
  .front-brand .brand-name {
    color: var(--leaf-green); font-weight: 700; font-size: 15px; text-align: center; line-height: 1.25;
  }
  .front-divider {
    position: absolute; left: 190px; top: 70px; width: 1px; height: 160px;
    background: var(--rule);
  }
  .contact {
    position: absolute; left: 222px; top: 86px; color: var(--ink-light);
  }
  .contact .person { color: var(--leaf-green); font-size: 24px; font-weight: 400; line-height: 1.1; }
  .contact .role { font-size: 13px; margin-top: 2px; }
  .contact .details { list-style: none; margin-top: 22px; font-size: 14px; line-height: 1.35; }
  .contact .label { color: var(--leaf-green); margin-right: 4px; }

  /* Back */
  .back-brand {
    position: absolute; left: 120px; top: 70px;
    display: flex; align-items: center; gap: 12px;
  }
  .back-brand .brand-dot { width: 44px; height: 44px; }
  .back-brand .brand-name { color: var(--leaf-green); font-weight: 700; font-size: 26px; line-height: 1; }
  .back-brand .tagline { color: var(--bark); font-size: 12px; letter-spacing: .5px; margin-top: 4px; }
  .field {
    position: absolute; color: var(--leaf-green); font-size: 14px;
    display: flex; align-items: flex-end; gap: 4px;
  }
  .field .blank { display: inline-block; border-bottom: 1px dashed var(--leaf-green); height: 14px; }
  .field-price { left: 300px; top: 150px; }
  .field-price .blank { width: 110px; }
  .field-start { left: 48px; top: 238px; }
  .field-start .blank { width: 140px; }
</style>
</head>
<body>
<main class="canvas">
  <section class="card card-front" aria-label="Card front">
    <div class="front-brand">
      <div class="brand-dot"></div>
      <div class="brand-name">Meridale Gardening</div>
    </div>
    <div class="front-divider"></div>
    <div class="contact">
      <h1 class="person">Trevor Kalbrook</h1>
      <p class="role">Horticulturalist</p>
      <ul class="details">
        <li><span class="label">T:</span>0452739186</li>
        <li><span class="label">E:</span>meridalegard@fernpost.com</li>
        <li><span class="label">W:</span>www.meridalegardening.com.au</li>
      </ul>
    </div>
  </section>

  <section class="card card-back" aria-label="Card back">
    <div class="back-brand">
      <div class="brand-dot"></div>
      <div>
        <div class="brand-name">Meridale Gardening</div>
        <div class="tagline">Garden Restorations &amp; Maintenance</div>
      </div>
    </div>
    <div class="field field-price">Price:<span class="blank"></span></div>
    <div class="field field-start">Start Date:<span class="blank"></span></div>
  </section>
</main>
</body>
</html>
```